Birchwell Entreprise Campus Media Package

We are looking for a designer to unify our company's image throughout its stationery and marketing deliverables. We will be focusing on:
*Business Cards (3.5 x 2)
*Letter Head (Letter Size)
*PowerPoint Presentation Template,
*One Pager Flyer (Letter Size)
*Front of Elevator's bay: 4 photos of the elevator bays (two groups of 3 elevators) to which we are looking for designs for its doors and surrounding wall (vinyl prints)
*Font's suggestions
*Official color palette.
*Outdoor Street Signage: please use the following dimensions:
Sign #1 (Richmond Side): 48(W)x72"(H) (3 sided)
Sign #2: 24"(W)x48"(H) (3 sided)
Sign #3 (Top of Hill): 30(W)x54(H) (2 sides)
*Carport Sign:
See photos attached. The white letters will be removed, and a new sign will take place. Preferably, Cut-Out fonts, but we can consider an alternative approach for cost effective solution.
Find attached the approved logos.
______________________________________
We are a real estate holding company focused on the commercial office space in the Ohio, US, market.
You can check our site at www.birchwellcampus-example.com
As inspiration guidelines, we would like to see designs that are modern, minimalistic, dynamic and energetic.
Updates
Target Market(s)
General Population, Business Owners, Non-Profit Organizations, Government
Industry/Entity Type
Real Estate - Commercial Office Space - Flex Space
Look and feel
Each slider illustrates characteristics of the customer's brand and the style your logo design should communicate.

```html
<!DOCTYPE html>
<html lang="en">
<head>
<meta charset="utf-8">
<title>Birchwell Entreprise Campus – Street Banner</title>
<link href="https://fonts.googleapis.com/css2?family=Montserrat:wght@400;600&display=swap" rel="stylesheet">
<style>
  :root {
    --navy-deep: #080f1a;
    --navy-mid: #0d1c2b;
    --teal-shade: #123246;
    --ink-white: #ffffff;
  }
  html, body {
    margin: 0;
    padding: 0;
    width: 1200px;
    height: 2516px;
    overflow: hidden;
    background: var(--ink-white);
  }
  .banner {
    position: relative;
    width: 1200px;
    height: 2516px;
    overflow: hidden;
    font-family: "Montserrat", Arial, sans-serif;
    color: var(--ink-white);
  }
  .banner-backdrop {
    position: absolute;
    inset: 0;
    background:
      radial-gradient(ellipse 70% 45% at 85% 30%, var(--teal-shade) 0%, transparent 70%),
      radial-gradient(ellipse 60% 40% at 20% 75%, #0f2536 0%, transparent 70%),
      linear-gradient(160deg, var(--navy-deep) 0%, var(--navy-mid) 55%, #0a1622 100%);
  }
  .banner-cut {
    position: absolute;
    left: 0;
    top: 0;
    width: 1200px;
    height: 2516px;
  }
  .brand-name {
    position: absolute;
    left: 0;
    width: 1200px;
    text-align: center;
    font-weight: 600;
    color: var(--ink-white);
    margin: 0;
  }
  .brand-name__main {
    top: 960px;
    font-size: 158px;
    letter-spacing: 2px;
    line-height: 1;
  }
  .brand-name__sub {
    top: 1180px;
    font-size: 72px;
    line-height: 1;
  }
  .contact {
    position: absolute;
    left: 0;
    top: 1625px;
    width: 1200px;
    text-align: center;
    font-weight: 600;
    font-size: 64px;
    line-height: 96px;
  }
  .contact__line {
    display: flex;
    justify-content: center;
    align-items: center;
    gap: 18px;
  }
  .contact__icon {
    width: 56px;
    height: 56px;
    fill: var(--ink-white);
  }
</style>
</head>
<body>
  <main class="banner">
    <div class="banner-backdrop" role="img" aria-label="Dark navy faceted geometric background"></div>

    <svg class="banner-cut" viewBox="0 0 1200 2516" aria-hidden="true">
      <polygon points="0,2516 1200,2236 1200,2516" fill="#ffffff"/>
    </svg>

    <p class="brand-name brand-name__main">BIRCHWELL</p>
    <p class="brand-name brand-name__sub">Entreprise Campus</p>

    <div class="contact">
      <div class="contact__line">
        <svg class="contact__icon" viewBox="0 0 24 24" aria-hidden="true">
          <path d="M6.6 10.8a15.1 15.1 0 0 0 6.6 6.6l2.2-2.2a1 1 0 0 1 1-.25 11.4 11.4 0 0 0 3.6.57 1 1 0 0 1 1 1V20a1 1 0 0 1-1 1A17 17 0 0 1 3 4a1 1 0 0 1 1-1h3.5a1 1 0 0 1 1 1c0 1.25.2 2.45.57 3.6a1 1 0 0 1-.25 1z"/>
        </svg>
        <span class="contact__phone">216.555.0142</span>
      </div>
      <div class="contact__line">
        <span class="contact__address">14800-14850 Harborline Av.</span>
      </div>
    </div>
  </main>
</body>
</html>
```